Dog Walking logo design

Dog Walking, Dog Sitting, Pet Taxi, Doggy Day Care. I'm looking for a design that shows a man walking 3 dogs. The dogs are on leads and we only see the mans legs. I'm open to suggestion re: the image of a sole of a boot associated with walking. I would like my company name as part of or incorporated into any image or logo.

Industry/Entity Type

It Company

Contact Information for Business Card

Milo the Pup Strider
Contact: www.milothepupstrider.example
Tel: 07912 358264

```html
<!DOCTYPE html>
<html lang="en">
<head>
<meta charset="utf-8">
<title>Milo the Pup Strider – Business Cards</title>
<link href="https://fonts.googleapis.com/css2?family=Source+Sans+3:wght@400;600;700&display=swap" rel="stylesheet">
<style>
  :root {
    --stage: #2e2e2e;
    --card-white: #ffffff;
    --brand-red: #8a0c18;
    --charcoal: #3a3a3c;
    --ink-light: #ffffff;
    --font-text: "Source Sans 3", "Myriad Pro", Arial, sans-serif;
  }
  * { box-sizing: border-box; margin: 0; padding: 0; }
  html, body {
    width: 1200px;
    height: 999px;
    overflow: hidden;
    background: var(--stage);
    font-family: var(--font-text);
  }
  .stage { position: relative; width: 1200px; height: 999px; }

  .card {
    position: absolute;
    width: 800px;
    height: 460px;
    overflow: hidden;
    box-shadow: 0 6px 18px rgba(0,0,0,0.45);
  }

  /* Front card */
  .card--front { left: 80px; top: 40px; background: var(--card-white); }
  .card__top {
    height: 300px;
    display: flex;
    align-items: center;
    justify-content: center;
  }
  .card__divider { height: 8px; background: var(--charcoal); }
  .card__bottom {
    height: 152px;
    background: var(--brand-red);
    color: var(--ink-light);
    position: relative;
  }
  .holder { position: absolute; left: 44px; top: 30px; }
  .holder__name { font-size: 34px; font-weight: 600; line-height: 1.1; }
  .holder__role { font-size: 18px; font-weight: 400; margin-top: 8px; }
  .contact { position: absolute; right: 52px; top: 10px; }
  .contact__tel { font-size: 24px; font-weight: 400; }
  .contact__web { font-size: 18px; font-weight: 400; margin-top: 2px; }

  /* Brand lockup */
  .brand { display: flex; align-items: center; gap: 22px; }
  .brand__mark { width: 64px; height: 64px; flex: none; }
  .brand__name {
    font-family: var(--font-text);
    font-weight: 700;
    font-size: 48px;
    line-height: 1;
    letter-spacing: 0.5px;
  }
  .brand--dark .brand__mark { background: var(--charcoal); }
  .brand--dark .brand__name { color: var(--brand-red); }
  .brand--light .brand__mark { background: var(--ink-light); width: 80px; height: 80px; }
  .brand--light .brand__name { color: var(--ink-light); font-size: 58px; }

  /* Back card */
  .card--back {
    left: 310px;
    top: 500px;
    background: var(--brand-red);
    display: flex;
    align-items: center;
    justify-content: center;
  }
</style>
</head>
<body>
<main class="stage">
  <section class="card card--front">
    <div class="card__top">
      <div class="brand brand--dark">
        <span class="brand__mark"></span>
        <span class="brand__name">Milo the Pup Strider</span>
      </div>
    </div>
    <div class="card__divider"></div>
    <div class="card__bottom">
      <div class="holder">
        <p class="holder__name">Name Title</p>
        <p class="holder__role">designation</p>
      </div>
      <div class="contact">
        <p class="contact__tel">Tel: 07912 358264</p>
        <p class="contact__web">www.milothepupstrider.example</p>
      </div>
    </div>
  </section>

  <section class="card card--back">
    <div class="brand brand--light">
      <span class="brand__mark"></span>
      <span class="brand__name">Milo the Pup Strider</span>
    </div>
  </section>
</main>
</body>
</html>
```